Web site for small printshop

I am looking for a website for small printshop in Iceland, mainly serving university students and artist.

We print posters, flyers, business cards and more.

In addition to our current website, I would like to include design tool, (fx. www.quarvelink.com, www.tandorizo.com or something similar) jobs upload, shopping chart.
Updates

Great work, I am really amazed of the quality of work i am seeing here.

Really way beyond my expectation

GOOD JOB - all of you ! 

Hi all.

The designs submitted have been great, way better than expected.
I really did not expect this level of quality.

Some have been asking me for feedback on their designs, and I will try 
to send some feedback here, without spoiling your creativity.

Likes:
- when the colors of my logo is used in menus, buttons etc.
- simple, not to crowded look.

Dislikes.
- Dark and heavy design
- Lot of text and buttons (crowded look)

Extra info.
- top line (before menus) will contain: Tel - email - language
- menu line will have 5 categories: Home - service - submission of works - FAQ - about us
- 3 large buttons:  Job submit - Job design - ask for offer

LOVE YOUR WORK - great designs so far :)

Target Market(s)

University Students, Artists. Age group 20-30

Industry/Entity Type

University

Requirements
Must have
• The website must be easy to use, clean looking.

```html
<!DOCTYPE html>
<html lang="en">
<head>
<meta charset="utf-8">
<title>Vellirprent – Business Cards</title>
<link href="https://fonts.googleapis.com/css2?family=Questrial&display=swap" rel="stylesheet">
<style>
:root{
  --stage:#000000;
  --white:#ffffff;
  --nav:#a8bdf2;
  --nav-line:#8ea6dd;
  --panel:#dfe3f7;
  --row-line:#b9bccb;
  --ink:#1a1a1a;
  --muted:#555555;
  --title:#7b7876;
  --btn:#c3cbf3;
  --btn-text:#8b8fa8;
  --footer:#555759;
  --footer-ink:#2b2b2b;
  --orange:#f5a21d;
  --orange-dark:#e06d12;
  --logo-square:#e8402a;
}
*{box-sizing:border-box;margin:0;padding:0}
html,body{width:953px;height:1200px;overflow:hidden;background:var(--stage);font-family:"Questrial",sans-serif}
.page{position:absolute;left:168px;top:0;width:620px;height:1200px;background:var(--panel)}
.header{position:absolute;left:0;top:0;width:620px;height:96px;background:var(--white);border-bottom:2px solid #cfd3e0}
.brand{position:absolute;left:22px;top:29px;display:flex;align-items:center;gap:10px}
.brand-mark{width:28px;height:34px;background:var(--logo-square)}
.brand-name{font-size:23px;font-weight:400;color:var(--ink);letter-spacing:.5px}
.search{position:absolute;left:416px;top:37px;width:182px;height:20px;border-radius:10px;background:linear-gradient(var(--orange),var(--orange-dark));display:flex;align-items:center;padding-left:6px}
.search-label{font-size:10px;font-weight:700;color:var(--ink);margin-right:4px}
.search-field{width:118px;height:11px;background:var(--white);border-radius:2px}
.search-go{margin-left:6px}
.nav{position:absolute;left:0;top:98px;width:620px;height:51px;background:var(--nav);border-top:1px solid var(--nav-line);border-bottom:2px solid var(--nav-line);display:flex}
.nav a{color:var(--white);text-decoration:none;font-size:20px;display:flex;align-items:center;justify-content:center;border-right:2px solid var(--nav-line);height:100%}
.nav a:last-child{border-right:none}
.social{position:absolute;top:155px;display:block;width:33px;height:34px;border-radius:6px;border:2px solid #cfd6f0}
.social.one{left:527px;background:#3b5a9a}
.social.two{left:574px;background:#3fa9e0}
.title{position:absolute;left:0;top:186px;width:620px;text-align:center;font-size:40px;color:var(--title);letter-spacing:1px}
.toolbar{position:absolute;top:266px;font-size:12px;color:var(--ink)}
.row{position:absolute;left:0;width:620px;height:82px;border-top:1px solid var(--row-line);border-bottom:1px solid var(--row-line)}
.thumb{position:absolute;left:42px;top:13px;width:98px;height:55px}
.card-name{position:absolute;left:152px;top:11px;font-size:13px;color:var(--ink)}
.card-desc{position:absolute;left:148px;top:28px;width:210px;font-size:10px;line-height:12px;color:var(--muted)}
.btn{position:absolute;left:510px;width:96px;height:19px;background:var(--btn);color:var(--btn-text);font-size:13px;text-align:center;line-height:19px}
.btn.details{top:6px}
.btn.wish{top:30px}
.price{position:absolute;right:16px;top:58px;font-size:12px;color:var(--ink)}
.paging{position:absolute;right:16px;top:989px;font-size:12px;color:var(--ink)}
.footer{position:absolute;left:0;top:1024px;width:620px;height:176px;background:var(--footer);display:flex}
.footer-col{width:206px;text-align:center;padding-top:16px}
.footer-col h3{font-size:20px;font-weight:400;color:var(--footer-ink);-webkit-text-stroke:.5px #888;margin-bottom:6px}
.footer-col p{font-size:16px;line-height:30px;color:var(--white)}
.footer-col p span{border-bottom:1px solid #888;padding-bottom:2px}
</style>
</head>
<body>
<div class="page">
  <header class="header">
    <div class="brand"><span class="brand-mark"></span><span class="brand-name">VELLIRPRENT</span></div>
    <div class="search">
      <span class="search-label">Search</span>
      <span class="search-field"></span>
      <svg class="search-go" width="22" height="12" viewBox="0 0 22 12"><path d="M3 1l5 5-5 5M11 1l5 5-5 5" fill="none" stroke="#fff" stroke-width="2.5"/></svg>
    </div>
  </header>
  <nav class="nav">
    <a style="width:110px">home</a>
    <a style="width:141px">about us</a>
    <a style="width:111px">service</a>
    <a style="width:148px">contact us</a>
    <a style="width:110px">prices</a>
  </nav>

  <span class="social one" role="img" aria-label="social network link"></span>
  <span class="social two" role="img" aria-label="social network link"></span>

  <h1 class="title">BUSINESS CARDS</h1>
  <div class="toolbar" style="left:15px">Display: List/Grind</div>
  <div class="toolbar" style="left:412px">Sort By:</div>
  <div class="toolbar" style="left:558px">Show:</div>

  <div class="row" style="top:292px">
    <div class="thumb" role="img" aria-label="black business card design" style="background:#050505"></div>
    <div class="card-name">Business Card Name</div>
    <div class="card-desc">Lorem ipsum dolor sit amet, consectetur adipisicing elit, sed do eiusmod tempor incididunt ut labore</div>
    <div class="btn details">view details</div><div class="btn wish">add to wish list</div>
    <div class="price">10$</div>
  </div>
  <div class="row" style="top:388px">
    <div class="thumb" role="img" aria-label="lime green business card design" style="background:#b6d300"></div>
    <div class="card-name">Business Card Name</div>
    <div class="card-desc">Lorem ipsum dolor sit amet, consectetur adipisicing elit, sed do eiusmod tempor incididunt ut labore</div>
    <div class="btn details">view details</div><div class="btn wish">add to wish list</div>
    <div class="price">10$</div>
  </div>
  <div class="row" style="top:487px">
    <div class="thumb" role="img" aria-label="orange to dark red business card design" style="background:linear-gradient(#f07a1c,#b0201a 60%,#3a0707)"></div>
    <div class="card-name">Business Card Name</div>
    <div class="card-desc">Lorem ipsum dolor sit amet, consectetur adipisicing elit, sed do eiusmod tempor incididunt ut labore</div>
    <div class="btn details">view details</div><div class="btn wish">add to wish list</div>
    <div class="price">10$</div>
  </div>
  <div class="row" style="top:589px">
    <div class="thumb" role="img" aria-label="white and blue business card design" style="background:linear-gradient(60deg,#5bb7e6,#ffffff 55%)"></div>
    <div class="card-name">Business Card Name</div>
    <div class="card-desc">Lorem ipsum dolor sit amet, consectetur adipisicing elit, sed do eiusmod tempor incididunt ut labore</div>
    <div class="btn details">view details</div><div class="btn wish">add to wish list</div>
    <div class="price">10$</div>
  </div>
  <div class="row" style="top:691px">
    <div class="thumb" role="img" aria-label="grey business card design" style="background:#8c8c8c"></div>
    <div class="card-name">Business Card Name</div>
    <div class="card-desc">Lorem ipsum dolor sit amet, consectetur adipisicing elit, sed do eiusmod tempor incididunt ut labore</div>
    <div class="btn details">view details</div><div class="btn wish">add to wish list</div>
    <div class="price">10$</div>
  </div>
  <div class="row" style="top:792px">
    <div class="thumb" role="img" aria-label="red business card design" style="background:#e3000f"></div>
    <div class="card-name">Business Card Name</div>
    <div class="card-desc">Lorem ipsum dolor sit amet, consectetur adipisicing elit, sed do eiusmod tempor incididunt ut labore</div>
    <div class="btn details">view details</div><div class="btn wish">add to wish list</div>
    <div class="price">10$</div>
  </div>
  <div class="row" style="top:894px">
    <div class="thumb" role="img" aria-label="orange business card design" style="background:#f39c00"></div>
    <div class="card-name">Business Card Name</div>
    <div class="card-desc">Lorem ipsum dolor sit amet, consectetur adipisicing elit, sed do eiusmod tempor incididunt ut labore</div>
    <div class="btn details">view details</div><div class="btn wish">add to wish list</div>
    <div class="price">10$</div>
  </div>

  <div class="paging">showing 1 to 7 of 7 (1 pages)</div>

  <footer class="footer">
    <div class="footer-col"><h3>ABOUT US</h3><p><span>Lorem ipsum dolor sit</span><br>amet, consectetur<br>adipisicing elit, sed do<br>eiusmod tempor...</p></div>
    <div class="footer-col"><h3>DID YOU KNOW</h3><p><span>Lorem ipsum dolor sit</span><br>amet, consectetur<br>adipisicing elit, sed do<br>eiusmod tempor...</p></div>
    <div class="footer-col"><h3>NEW PUBLICATIONS</h3><p><span>Lorem ipsum dolor sit</span><br>amet, consectetur<br>adipisicing elit, sed do<br>eiusmod tempor...</p></div>
  </footer>
</div>
</body>
</html>
```